Letterhead and envelope design

Using current logo and colours I would like to have a new design done for a stationary set to be printed.

The new files should include logo, web and email address as well as,mailing address and phone number

Dov Harmsby
Harmsby Construction Inc
Box 27 Site 18 RR5
Okotoks AB
T4K 2B9
Cell : 403-555-2917
Email: dov@harmsbyconstruction.example
web: harmsbyconstruction.example

```html
<!DOCTYPE html>
<html lang="en">
<head>
<meta charset="utf-8">
<title>Harmsby Construction – Letterhead</title>
<link rel="stylesheet" href="https://fonts.googleapis.com/css2?family=Roboto:wght@400;500;700&display=swap">
<style>
  :root {
    --navy: #003366;
    --orange: #e8991e;
    --ink: #333333;
    --backdrop: #b8b8b8;
    --paper: #ffffff;
    --faint: #ececec;
  }
  * { box-sizing: border-box; margin: 0; padding: 0; }
  html, body {
    width: 911px; height: 1200px; overflow: hidden;
    background: var(--backdrop);
    font-family: "Roboto", Arial, sans-serif;
  }
  .sheet {
    position: absolute; left: 70px; top: 61px;
    width: 762px; height: 1079px;
    background: var(--paper); overflow: hidden;
  }
  .rule { position: absolute; top: 86px; height: 3px; background: var(--orange); }
  .rule--left { left: 0; width: 58px; }
  .rule--right { left: 213px; right: 0; }
  .brand-disc {
    position: absolute; left: 67px; top: 19px;
    width: 136px; height: 136px; border-radius: 50%;
    background: var(--navy);
  }
  .brand-name {
    position: absolute; left: 223px; top: 46px;
    font-size: 33px; font-weight: 500; color: var(--navy);
    letter-spacing: -0.3px; line-height: 40px; white-space: nowrap;
  }
  .backdrop-disc {
    position: absolute; left: 189px; top: 354px;
    width: 388px; height: 388px; border-radius: 50%;
    background: var(--faint); opacity: 0.7;
  }
  .letter { position: absolute; left: 70px; width: 621px; color: var(--ink); }
  .letter__date {
    position: absolute; right: 71px; top: 209px;
    font-size: 17px; color: var(--ink);
  }
  .letter__greeting { top: 248px; font-size: 17px; }
  .letter__body { top: 287px; font-size: 15.2px; line-height: 21.7px; }
  .letter__body p { text-align: justify; margin-bottom: 21.7px; }
  .letter__closing { top: 757px; font-size: 17px; }
  .signature {
    position: absolute; left: 63px; top: 793px;
    width: 125px; height: 50px; border-radius: 6px;
    background: #e4e4e4;
  }
  .address-tab {
    position: absolute; left: 221px; top: 993px;
    width: 316px; height: 30px;
    background: var(--orange); border-radius: 12px 12px 0 0;
    display: flex; align-items: center; gap: 8px; padding-left: 14px;
    color: var(--navy); font-weight: 700; font-size: 12.5px; white-space: nowrap;
  }
  .contact-band {
    position: absolute; left: 0; right: 0; top: 1022px; bottom: 0;
    background: var(--navy); border-top: 3px solid var(--orange);
    display: flex; justify-content: center; align-items: flex-start;
    gap: 34px; padding-top: 14px;
  }
  .contact {
    display: flex; align-items: center; gap: 8px; flex: none;
    color: #fff; font-size: 13px; font-weight: 500; white-space: nowrap;
  }
  .contact__icon {
    width: 26px; height: 26px; border-radius: 50%; flex: none;
    background: var(--orange);
    display: flex; align-items: center; justify-content: center;
  }
</style>
</head>
<body>
  <div class="sheet">
    <div class="rule rule--left"></div>
    <div class="rule rule--right"></div>
    <div class="brand-disc"></div>
    <div class="brand-name">HARMSBY CONSTRUCTION</div>

    <div class="backdrop-disc"></div>

    <div class="letter__date">XX-XX-XXXX</div>
    <div class="letter letter__greeting">Dear Clients</div>
    <div class="letter letter__body">
      <p>Lorem ipsum dolor sit amet, consectetur adipiscing elit, sed do eiusmod tempor incididunt ut labore et dolore magna aliqua. Ut enim ad minim veniam, quis nostrud exercitation ullamco laboris nisi ut aliquip ex ea commodo consequat. Duis aute irure dolor in reprehenderit in voluptate velit esse cillum dolore eu fugiat nulla pariatur. Excepteur sint occaecat cupidatat non proident, sunt in culpa qui officia deserunt mollit anim id est laborum.</p>
      <p>Lorem ipsum dolor sit amet, consectetur adipiscing elit, sed do eiusmod tempor incididunt ut labore et dolore magna aliqua. Ut enim ad minim veniam, quis nostrud exercitation ullamco laboris nisi ut aliquip ex ea commodo consequat. Duis aute irure dolor in reprehenderit in voluptate velit esse cillum dolore eu fugiat nulla pariatur. Excepteur sint occaecat cupidatat non proident, sunt in culpa qui officia deserunt mollit anim id est laborum.</p>
      <p>Lorem ipsum dolor sit amet, consectetur adipiscing elit, sed do eiusmod tempor incididunt ut labore et dolore magna aliqua. Ut enim ad minim veniam, quis nostrud exercitation ullamco laboris nisi ut aliquip ex ea commodo consequat. Duis aute irure dolor in reprehenderit in voluptate velit esse cillum dolore eu fugiat nulla pariatur. Excepteur sint occaecat cupidatat non proident, sunt in culpa qui officia deserunt mollit anim id est laborum.</p>
    </div>
    <div class="letter letter__closing">Sincerly,</div>
    <div class="signature" role="img" aria-label="Handwritten signature"></div>

    <div class="address-tab">
      <svg width="12" height="16" viewBox="0 0 12 16" aria-hidden="true">
        <path d="M6 0C2.7 0 0 2.6 0 5.9 0 10.3 6 16 6 16s6-5.7 6-10.1C12 2.6 9.3 0 6 0zm0 8.2A2.3 2.3 0 1 1 6 3.6a2.3 2.3 0 0 1 0 4.6z" fill="#003366"/>
      </svg>
      <span>BOX 27 SITE 18 RR5 OKOTOKS AB T4K 2B9</span>
    </div>

    <div class="contact-band">
      <div class="contact contact--web">
        <span class="contact__icon">
          <svg width="15" height="15" viewBox="0 0 16 16" fill="none" stroke="#003366" stroke-width="1.4" aria-hidden="true">
            <circle cx="8" cy="8" r="6.5"/><ellipse cx="8" cy="8" rx="3" ry="6.5"/><path d="M1.5 8h13M2.5 4.8h11M2.5 11.2h11"/>
          </svg>
        </span>
        <span>www.harmsbyconstruction.example</span>
      </div>
      <div class="contact contact--phone">
        <span class="contact__icon">
          <svg width="14" height="14" viewBox="0 0 16 16" aria-hidden="true">
            <path d="M3.6 1.2l2.2 2.8-1.3 1.6c.9 2 2.4 3.5 4.4 4.4l1.6-1.3 2.8 2.2-1.2 2.5C7.3 13.5 2.5 8.7 1.1 3z" fill="#003366"/>
          </svg>
        </span>
        <span>403-555-2917</span>
      </div>
      <div class="contact contact--email">
        <span class="contact__icon">
          <svg width="14" height="11" viewBox="0 0 16 12" aria-hidden="true">
            <rect x="0.5" y="0.5" width="15" height="11" rx="1.5" fill="#003366"/>
            <path d="M1.5 1.8L8 6.8l6.5-5" fill="none" stroke="#e8991e" stroke-width="1.3"/>
          </svg>
        </span>
        <span>dov@harmsbyconstruction.example</span>
      </div>
    </div>
  </div>
</body>
</html>
```